create clean, simple business card template

using the logo created now we need to create a simple, elegant business card design to suit

Industry/Entity Type

Business

Font styles to use
Other font styles liked:
• segoe ui

Requirements
Must have
• Front:
"Name:"
"Title:"
"Mobile:"
"email:"
and the logo

Back:
Logo
Nice to have
• Text in black but other graphics etc to match colours in logo as provided

```html
<!DOCTYPE html>
<html lang="en">
<head>
<meta charset="UTF-8">
<title>Kestrel Homes – Business Card</title>
<link rel="stylesheet" href="https://fonts.googleapis.com/css2?family=Open+Sans:wght@400;600;700&display=swap">
<style>
  :root {
    --backdrop: #b7e3e4;
    --card: #ffffff;
    --charcoal: #2e3429;
    --gold: #8f7a2c;
    --ink: #111111;
  }
  * { box-sizing: border-box; margin: 0; padding: 0; }
  html, body {
    width: 1200px;
    height: 1000px;
    overflow: hidden;
  }
  body {
    background: var(--backdrop);
    font-family: "Open Sans", "Segoe UI", sans-serif;
    position: relative;
  }
  .card {
    position: absolute;
    background: var(--card);
    overflow: hidden;
    box-shadow: 0 3px 10px rgba(0,0,0,0.18);
  }
  .card--front { left: 100px; top: 50px; width: 800px; height: 450px; }
  .card--back  { left: 300px; top: 520px; width: 795px; height: 445px; }

  .swoosh { position: absolute; inset: 0; width: 100%; height: 100%; }

  .brand {
    position: absolute;
    display: flex;
    align-items: center;
    gap: 14px;
  }
  .brand__dot {
    width: 34px; height: 34px;
    border-radius: 50%;
    background: var(--charcoal);
  }
  .brand__name {
    font-family: "Open Sans", "Segoe UI", sans-serif;
    font-weight: 600;
    color: var(--gold);
    white-space: nowrap;
  }
  .card--front .brand { left: 230px; top: 100px; }
  .card--front .brand__name { font-size: 44px; }
  .card--back .brand { left: 70px; top: 195px; }
  .card--back .brand__dot { width: 42px; height: 42px; }
  .card--back .brand__name { font-size: 54px; }

  .contact {
    position: absolute;
    left: 392px;
    top: 268px;
    color: var(--ink);
  }
  .contact__name {
    font-weight: 700;
    font-size: 30px;
    margin-bottom: 10px;
  }
  .contact__line {
    font-weight: 400;
    font-size: 19px;
    line-height: 1.5;
  }

  .skyline {
    position: absolute;
    left: 0; right: 0; bottom: 0;
    height: 150px;
    background: linear-gradient(to top, var(--gold) 70%, #9a8638 100%);
  }
</style>
</head>
<body>
  <section class="card card--front">
    <svg class="swoosh" viewBox="0 0 800 450" aria-hidden="true">
      <ellipse cx="430" cy="170" rx="470" ry="320" fill="var(--charcoal)"/>
      <ellipse cx="470" cy="140" rx="420" ry="260" fill="var(--card)"/>
      <path d="M0 0 H800 V40 C600 -10 200 -10 0 40 Z" fill="var(--card)"/>
    </svg>
    <div class="brand">
      <span class="brand__dot"></span>
      <span class="brand__name">Kestrel Homes</span>
    </div>
    <div class="contact">
      <p class="contact__name">Adrian Hollis</p>
      <p class="contact__line">+91 9876501234</p>
      <p class="contact__line">hello@kestrelhomes.org</p>
    </div>
  </section>

  <section class="card card--back">
    <div class="brand">
      <span class="brand__dot"></span>
      <span class="brand__name">Kestrel Homes</span>
    </div>
    <div class="skyline" role="img" aria-label="Gold city skyline silhouette along the bottom edge"></div>
  </section>
</body>
</html>
```